We need a mobile and desktop design for our new online store, Ripper Rustic. The website's goals is to help Australian manufacturers and inventors sell their goods online.

The site needs to match the them of our logo.
Updates

Reason: We are extending the deadline because we have been away for Easter and was unable to answer everyone's questions.

Thank you for everyone's questions. I'm sorry for the delay in my answer. I have been away. We do not need the site coded. My coders have asked for a graphic they can cut up.

While we don't need anyone to code the site. If the choosen designer does a great job and is easy to work with, it highly likely we will hire them for future work. We have been running a business online for ten years and are short a graphic designer at the moment. It is fair to think of this as the first stage of a job interview.

The target market is Australian consumers. The website is a marketing portal for Australian producers/manufacturers/inventors to sell their goods online.

We will be helping companies who are brilliant at making goods but need some help selling them online.

Each company will have it''s own store on the site. The companies lined up so far include a chocolate manufacturer, kitchen sponge manufacturer, curry producer and surfboard maker. The range of stores will vary. We are looking for an overall design to work from.

We are basins the function of the store design on BrainFizz.com store and our existing store you can view at www.tidypurse.com.au/store. I also like Green Kite days and Wombuy.com.au

I'm sorry, we are not going to guarantee payment. Just in case, none of the designs are appropriate. But, this is the third time we have used Pixel Gather and we paid for both previous jobs. We are not here to waste time.

If you have any more questions. Fire away. I''m sorry, my last brief was a bit too brief. It was my last task before rushing to a school presentation.

I'm looking forward to seeing everyone's designs and hopefully meeting a new designer.

Here is a link to our first mock up of the site created by our coders. Ignore the graphics and text. (It was the boys putting something there to work from.) The URL is:-

www.ripperrustic.com

The stores motto is...

"We only sell goods that are Ripper Rustic!"

Our goals are..

To help Australian manufacturers, inventors and producers. People who are good at making items and are adding value to Australia, but are so busy making their goods that they struggle selling them online.

Of the designs we have seen so far, I prefer the blue and white based designs, instead of the red adn white. Because, the red ones seem to make the site look more bloody then brilliant :-)

All businesses/stores will be given a Gold, Bronze or Silver ranking, depending on how much of their work benefits Australia.

Thank you for everyone's designs so far. The quality of the designs have been excellent! Our team will be discussing them on Thursday. I'll post an update on Friday morning

All the best,

Maree

Target Market(s)

Australians, general

Industry/Entity Type

Store

Requirements
Must have
• Online store

```html
<!DOCTYPE html>
<html lang="en">
<head>
<meta charset="utf-8">
<title>Ripper Rustic – Store Home</title>
<link href="https://fonts.googleapis.com/css2?family=Arimo:wght@400;700&display=swap" rel="stylesheet">
<style>
:root{
  --bg:#ebebeb;
  --page:#ffffff;
  --blue-hi:#3cbcf0;
  --blue:#1a9ad8;
  --blue-lo:#0b84c4;
  --navy:#0d3f78;
  --heading:#0b6db5;
  --link:#1a5ea8;
  --price:#3a9f0c;
  --text:#555;
  --muted:#777;
  --panel:#efefef;
  --panel-line:#d5d5d5;
  --card:#f4f5f7;
  --fb:#4a67ad;
  --dark-btn:#4a4a4a;
}
*{box-sizing:border-box;margin:0;padding:0}
html,body{width:952px;height:1200px;overflow:hidden}
body{background:var(--bg);font-family:"Arimo",Arial,sans-serif;color:var(--text);font-size:11px}
.canvas{position:relative;width:952px;height:1200px;overflow:hidden}
.page{position:absolute;left:71px;top:0;width:810px;height:1134px;background:var(--page)}
.abs{position:absolute}

/* header */
.brand{left:73px;top:20px;width:170px;color:var(--navy);font-weight:700;font-size:31px;line-height:33px;letter-spacing:-.5px}
.account{left:432px;top:17px;font-size:11px;color:#444;display:flex;gap:8px;align-items:center}
.account svg{vertical-align:-2px;margin-right:3px}
.search{left:690px;top:12px;width:191px;height:23px;border:1px solid #ccc;background:#fff;font-size:9px;color:#999;padding:5px 10px}
.search svg{position:absolute;right:7px;top:4px}
.nav{left:232px;top:50px;width:644px;height:66px;border-radius:4px;background:linear-gradient(var(--blue-hi),var(--blue) 60%,var(--blue-lo));display:flex;padding-left:30px;box-shadow:0 1px 2px rgba(0,0,0,.25)}
.nav a{color:#fff;text-decoration:none;font-weight:700;font-size:11.5px;display:flex;align-items:center;justify-content:center;border-left:1px solid rgba(255,255,255,.25)}
.nav a.active{background:rgba(0,80,150,.25)}

/* sidebar */
.newsletter{left:79px;top:124px;width:207px;height:196px;border-radius:3px;background:linear-gradient(var(--blue-hi),var(--blue-lo))}
.newsletter h2{position:absolute;left:0;right:0;top:11px;text-align:center;color:var(--navy);font-size:17px;font-weight:700}
.newsletter .field{position:absolute;left:10px;top:40px;width:187px;height:27px;background:#fff;border:1px solid #bcd;font-size:8.5px;color:#666;padding:9px 9px}
.newsletter .btn{position:absolute;left:113px;top:78px;width:84px;height:27px;border-radius:4px;background:linear-gradient(#1b5fa6,#0c3f7c);color:#fff;font-weight:700;font-size:11.5px;display:flex;align-items:center;justify-content:center}
.newsletter .divider{position:absolute;left:0;right:0;top:119px;border-top:1px solid rgba(255,255,255,.35)}
.promo{position:absolute;left:7px;top:133px;width:193px;height:49px;background:linear-gradient(90deg,#0c4d8c,#2a8fd0)}

.panel{background:var(--panel);border:1px solid var(--panel-line);border-radius:3px}
.panel h3{font-size:15px;font-weight:700;color:#666;padding:11px 10px 0;height:40px;border-bottom:1px solid #dcdcdc}
.categories{left:79px;top:327px;width:207px;height:479px}
.categories ul{list-style:none;padding:10px 0 0 19px}
.categories li{height:23.2px;font-size:11px;color:#777;line-height:23.2px}
.categories li::before{content:"•";color:#999;margin-right:6px}
.gifts{left:79px;top:812px;width:207px;height:192px}
.gifts .box{position:absolute;left:10px;top:51px;width:188px;height:129px;background:#fff}
.gifts .art{position:absolute;left:6px;top:9px;width:92px;height:120px;background:linear-gradient(#c9b88c,#9aa088 50%,#eee 70%)}
.gifts p{position:absolute;left:113px;top:50px;color:var(--link);font-size:11px;line-height:15px}

/* main */
.hero{left:296px;top:128px;width:578px;height:192px;border:3px solid #e8e8e8;border-radius:3px;background:linear-gradient(90deg,#f2f2f2,#dedede)}
.hero h1{position:absolute;left:22px;top:58px;font-size:18px;font-weight:400;color:#333}
.hero .more{position:absolute;left:22px;top:86px;width:84px;height:27px;border-radius:3px;background:linear-gradient(#666,var(--dark-btn));color:#fff;font-weight:700;font-size:11.5px;display:flex;align-items:center;justify-content:center}
.hero .dots{position:absolute;left:22px;top:160px;display:flex;gap:6px}
.hero .dots i{width:11px;height:11px;border-radius:50%;background:#333;border:2px solid #fff;box-shadow:0 0 1px #888}
.hero .dots i.on{background:#1a8fd8}
.hero .photo{position:absolute;left:395px;top:6px;width:177px;height:177px;background:linear-gradient(#8a8285,#c9a77a 70%,#d8d8d8)}

.section-title{color:var(--heading);font-size:15px;font-weight:700}
.rule{height:1px;background:#e3e3e3}
.arrow-btn{left:858px;top:340px}

.card{top:380px;width:181px;height:181px;background:var(--card);border:1px solid #dedede}
.card .thumb{position:absolute;left:6px;top:5px;width:169px;height:103px;background:#fff}
.card .thumb div{position:absolute;left:55px;top:9px;width:60px;height:88px}
.card .name{position:absolute;left:10px;top:117px;color:var(--link);font-size:11px}
.card .price{position:absolute;left:10px;top:132px;color:var(--price);font-size:11px}
.card .desc{position:absolute;left:10px;top:147px;width:160px;font-size:10px;line-height:15px;color:#666;text-align:justify}

.row{left:296px;width:578px;height:115px;background:var(--card);border:1px solid #dedede}
.row .thumb{position:absolute;left:5px;top:5px;width:120px;height:104px;background:#fff}
.row .thumb div{position:absolute;left:23px;top:10px;width:75px;height:88px}
.row .name{position:absolute;left:137px;top:10px;color:var(--link);font-size:11px}
.row .price{position:absolute;left:137px;top:25px;color:var(--price);font-size:11px}
.row .desc{position:absolute;left:137px;top:44px;width:432px;font-size:9.4px;line-height:16.5px;color:#666}

.pager{left:597px;top:986px;display:flex;gap:3px;align-items:center;font-size:8.5px;color:#666}
.pager span.lbl{margin-right:3px;letter-spacing:.5px}
.pager b{width:18px;height:17px;border-radius:3px;background:#d6d6d6;color:#999;font-weight:400;display:flex;align-items:center;justify-content:center;font-size:8px}
.pager b.on{background:#8a8a8a;color:#fff}
.pager b.wide{width:19px}

/* bottom row */
.social{left:77px;top:1023px;width:521px;height:103px;border-radius:3px;background:var(--fb)}
.social h2{position:absolute;left:17px;top:21px;color:#fff;font-size:17px;font-weight:700}
.social .share{position:absolute;left:54px;top:47px;width:105px;height:37px;border:2px solid #cfd9ef;border-radius:4px;background:linear-gradient(#5b78bb,#3f5c9e);color:#fff;font-family:"Arimo",Arial,sans-serif;font-size:14px;display:flex;align-items:center;justify-content:center;letter-spacing:.5px}
.social .widget{position:absolute;left:219px;top:8px;width:295px;height:88px;background:#fff;padding:5px}
.social .widget div{width:100%;height:100%;background:linear-gradient(90deg,#7a6a5f,#9f8b7d,#6d7f95,#a38d78,#c99a5f)}
.video{left:604px;top:1023px;width:271px;height:103px;border-radius:3px;background:#e4e4e4}
.video p{position:absolute;left:24px;top:31px;font-size:14px;font-weight:700;color:#888;line-height:17.5px}
.video .screen{position:absolute;left:91px;top:4px;width:177px;height:96px;border:3px solid #222;border-radius:4px;background:radial-gradient(circle at 50% 45%,#8d8f86,#4a4d48 75%)}
.video svg{position:absolute;left:70px;top:29px}

/* footer */
.footer-links{left:71px;top:1149px;font-size:10.5px;color:#666;display:flex;gap:8px}
.copy{left:71px;top:1176px;font-size:10.5px;color:#666}
.follow{left:800px;top:1163px;font-size:10.5px;color:var(--link);display:flex;gap:8px}
</style>
</head>
<body>
<div class="canvas">
  <div class="page"></div>

  <!-- header -->
  <div class="abs brand">Ripper<br>Rustic</div>
  <div class="abs account">
    <span><svg width="11" height="11" viewBox="0 0 11 11"><circle cx="5.5" cy="3" r="2.6" fill="#555"/><path d="M0.5 11c0-3.5 2.2-4.8 5-4.8s5 1.3 5 4.8z" fill="#555"/></svg>My Account</span>
    <span>|</span>
    <span><svg width="12" height="10" viewBox="0 0 12 10"><path d="M0 1h2l1.5 6h6.5l1.5-4.5H3" fill="none" stroke="#555" stroke-width="1.2"/><circle cx="4.5" cy="9" r="1" fill="#555"/><circle cx="9" cy="9" r="1" fill="#555"/></svg>My Cart &nbsp;(3) items - $25.00</span>
  </div>
  <div class="abs search">Search
    <svg width="13" height="13" viewBox="0 0 13 13"><circle cx="5" cy="5" r="3.6" fill="none" stroke="#222" stroke-width="2"/><path d="M7.7 7.7l4 4" stroke="#222" stroke-width="2.4"/></svg>
  </div>
  <nav class="abs nav">
    <a class="active" style="width:67px">HOME</a>
    <a style="width:71px">ABOUT</a>
    <a style="width:103px">ALL STORES</a>
    <a style="width:158px">SHIPPING &amp; ACCOUNTS</a>
    <a style="width:64px">BLOG</a>
    <a style="width:84px">CONTACT</a>
    <a style="width:67px">HELP</a>
  </nav>

  <!-- sidebar -->
  <section class="abs newsletter">
    <h2>Newsletter Subscribe</h2>
    <div class="field">Enter your mai IID</div>
    <div class="btn">SUBSCRIBE</div>
    <div class="divider"></div>
    <div class="promo" role="img" aria-label="TixHop ticket-selling partner banner"></div>
  </section>

  <section class="abs panel categories">
    <h3>Categories</h3>
    <ul>
      <li>Integer lobortis</li>
      <li>Curabitur ac malesuada</li>
      <li>Phasellus tellus nisl</li>
      <li>Aenean fringilla varius</li>
      <li>Vestibulum gravida</li>
      <li>Aliquam commodo</li>
      <li>Integer lobortis</li>
      <li>Curabitur ac</li>
      <li>Phasellus tellus nisl</li>
      <li>Aenean fringilla vestibulum</li>
      <li>Vestibulum</li>
      <li>Aliquam commodo</li>
      <li>Integer lobortis</li>
      <li>Curabitur ac</li>
      <li>Phasellus tellus nisl</li>
      <li>Aenean fringilla euismod</li>
      <li>Vestibulum</li>
      <li>Aliquam commodo</li>
    </ul>
  </section>

  <section class="abs panel gifts">
    <h3>Gift Ideas</h3>
    <div class="box">
      <div class="art" role="img" aria-label="Photo of stacked scrubbing sponges and a white gift box with ribbon"></div>
      <p>Pellentesque<br>elementum<br>tellus posuere</p>
    </div>
  </section>

  <!-- hero -->
  <section class="abs hero">
    <h1>We only sell goods that are Ripper Rustic!</h1>
    <div class="more">VIEW MORE</div>
    <div class="dots"><i class="on"></i><i></i><i></i><i></i></div>
    <div class="photo" role="img" aria-label="Photo of a timber-framed grey armchair with two small dogs sitting beneath"></div>
  </section>

  <!-- latest arrivals grid -->
  <h2 class="abs section-title" style="left:296px;top:339px">Latest Arrivals</h2>
  <svg class="abs arrow-btn" width="16" height="16" viewBox="0 0 16 16"><circle cx="8" cy="8" r="8" fill="#9a9a9a"/><path d="M6.5 4.5l3.5 3.5-3.5 3.5" fill="none" stroke="#fff" stroke-width="2"/></svg>
  <div class="abs rule" style="left:296px;top:367px;width:578px"></div>

  <article class="abs card" style="left:296px">
    <div class="thumb"><div role="img" aria-label="Product photo of a packaged fruit and vegetable kit with blue balls" style="background:linear-gradient(#e9b43a,#c8862d 55%,#2740a0)"></div></div>
    <div class="name">Etiam massa massa</div>
    <div class="price">$9.95 ($9.50)</div>
    <div class="desc">Phasellus pharetra velit sed tellus egestas fringilla.</div>
  </article>
  <article class="abs card" style="left:494px">
    <div class="thumb"><div role="img" aria-label="Product photo of a kraft paper refill pouch with vegetables" style="background:linear-gradient(#d1a25a,#b98440 60%,#7a8a3a)"></div></div>
    <div class="name">Etiam massa massa</div>
    <div class="price">$9.95 ($9.50)</div>
    <div class="desc">Phasellus pharetra velit sed tellus egestas fringilla.</div>
  </article>
  <article class="abs card" style="left:693px">
    <div class="thumb"><div role="img" aria-label="Product photo of a budgeting book cover with a piggy bank" style="left:57px;width:50px;background:linear-gradient(90deg,#c7762a,#f2f2f2 40%,#ffffff)"></div></div>
    <div class="name">Etiam massa massa</div>
    <div class="price">$9.95 ($9.50)</div>
    <div class="desc">Phasellus pharetra velit sed tellus egestas fringilla.</div>
  </article>

  <div class="abs rule" style="left:296px;top:574px;width:578px"></div>
  <h2 class="abs section-title" style="left:296px;top:586px">Latest Arrivals</h2>

  <article class="abs row" style="top:614px">
    <div class="thumb"><div role="img" aria-label="Product photo of a white two-tier toddler toilet seat" style="background:linear-gradient(#e6e8ea,#b5b9bd)"></div></div>
    <div class="name">Etiam massa massa</div>
    <div class="price">$9.95 ($9.50)</div>
    <div class="desc">Phasellus pharetra velit sed tellus egestas fringilla. Maecenas quis erat libero, non interdum eros. Aenean at nunc in neque fringilla malesuada. Quisque convallis mi vitae felis feugiat fermentum. Nam pharetra aliquam enim, non venenatis leo elementum a. Mauris interdum lobortis diam, vitae ultricies sem blandit a. Mauris ac urna dolor, nec sagittis lectus.</div>
  </article>
  <article class="abs row" style="top:736px">
    <div class="thumb"><div role="img" aria-label="Product photo of a hand spraying a wine preserver beside a bottle and glass" style="background:linear-gradient(90deg,#e8e8e8,#2a2a2a 45%,#6e1a1a 80%,#e8e8e8)"></div></div>
    <div class="name">Etiam massa massa</div>
    <div class="price">$9.95 ($9.50)</div>
    <div class="desc">Phasellus pharetra velit sed tellus egestas fringilla. Maecenas quis erat libero, non interdum eros. Aenean at nunc in neque fringilla malesuada. Quisque convallis mi vitae felis feugiat fermentum. Nam pharetra aliquam enim, non venenatis leo elementum a. Mauris interdum lobortis diam, vitae ultricies sem blandit a. Mauris ac urna dolor, nec sagittis lectus.</div>
  </article>
  <article class="abs row" style="top:859px">
    <div class="thumb"><div role="img" aria-label="Product photo of a handheld gaming device clipped to a belt" style="background:linear-gradient(#3c3a36,#c9695a 60%,#2d6b8a)"></div></div>
    <div class="name">Etiam massa massa</div>
    <div class="price">$9.95 ($9.50)</div>
    <div class="desc">Phasellus pharetra velit sed tellus egestas fringilla. Maecenas quis erat libero, non interdum eros. Aenean at nunc in neque fringilla malesuada. Quisque convallis mi vitae felis feugiat fermentum. Nam pharetra aliquam enim, non venenatis leo elementum a. Mauris interdum lobortis diam, vitae ultricies sem blandit a. Mauris ac urna dolor, nec sagittis lectus.</div>
  </article>

  <div class="abs pager">
    <span class="lbl">Page 1 of 32</span>
    <b class="on">1</b><b>2</b><b>3</b><b>4</b><b>5</b><b>6</b><b>7</b><b>8</b><b>»</b>
    <span style="margin:0 3px">···</span>
    <b class="wide">»»</b>
  </div>

  <!-- bottom row -->
  <section class="abs social">
    <h2>Like us on Chatterly</h2>
    <div class="share">SHARE</div>
    <div class="widget"><div role="img" aria-label="Grid of follower profile thumbnails in a social fan widget"></div></div>
  </section>
  <section class="abs video">
    <p>How it<br>works<br>Video</p>
    <div class="screen" role="img" aria-label="Video still of a product label close-up">
      <svg width="36" height="36" viewBox="0 0 36 36"><circle cx="18" cy="18" r="16" fill="#3a3a3a" stroke="#ddd" stroke-width="2.5"/><path d="M14 10l11 8-11 8z" fill="#eee"/></svg>
    </div>
  </section>

  <!-- footer -->
  <div class="abs footer-links">
    <span>Home</span><span>|</span><span>About</span><span>|</span><span>All Stores</span><span>|</span><span>Shipping &amp; Accounts</span><span>|</span><span>Blog</span><span>|</span><span>Contact</span><span>|</span><span>Help</span>
  </div>
  <div class="abs copy">Copyright &nbsp;© &nbsp;2013 &nbsp;&nbsp;www.ripperrustic.com &nbsp;&nbsp;All rights reserved.</div>
  <div class="abs follow"><span>Chatterly</span><span>Chirpr</span></div>
</div>
</body>
</html>
```